High Tech Real Estate Startup needs a business card

We are developing an innovative real estate marketing product based around advanced search and virtual reality.

We talk to people, we need business cards.

Target Market(s)

The target market is technology professionals and realtors.

Contact Information for Business Card

The information to be included will include

Name
Title
Phone Number
E-mail Address
www.quelzo.com

It should use simple iconography for each one of those fields.

Font styles to use
Other font styles liked:
• Co, Jubilat, Avenir

Colors

Designer to choose colors to be used in the design.

Requirements
Must have
• Clean aesthetic,
• Good use of negative space.
• It should use our company logo, shown in the attached file. It is able to use the negative of that logo (coloured font and white background) and I have attached other acceptable accent colours in a swatch file.
Should not have
• Should not be too busy
• No extraneous text (slogans, tag lines etc)

```html
<!DOCTYPE html>
<html lang="en">
<head>
<meta charset="UTF-8">
<title>Quelzo Business Card</title>
<link rel="stylesheet" href="https://fonts.googleapis.com/css2?family=Montserrat:wght@400;500;700&display=swap">
<style>
  :root {
    --backdrop: #2e3d46;
    --card-white: #ffffff;
    --brand-teal: #14b9bd;
    --ink: #1c1c1c;
  }
  * { margin: 0; padding: 0; box-sizing: border-box; }
  html, body {
    width: 1200px;
    height: 900px;
    overflow: hidden;
    background: var(--backdrop);
    font-family: "Montserrat", sans-serif;
  }
  .canvas {
    width: 1200px;
    height: 900px;
    display: flex;
    flex-direction: column;
    align-items: center;
    justify-content: center;
    gap: 48px;
  }
  .card {
    width: 600px;
    height: 343px;
    position: relative;
    box-shadow: 0 10px 30px rgba(0,0,0,0.35);
  }
  .card-front {
    background: var(--card-white);
    display: flex;
    flex-direction: column;
    align-items: center;
  }
  .card-front .frame {
    position: absolute;
    inset: 18px;
    border: 2.5px solid var(--brand-teal);
  }
  .person-name {
    margin-top: 78px;
    font-weight: 700;
    font-size: 34px;
    color: var(--ink);
    letter-spacing: 0.2px;
  }
  .name-rule {
    width: 118px;
    height: 3px;
    background: var(--brand-teal);
    margin-top: 12px;
  }
  .contact-line {
    margin-top: 22px;
    display: flex;
    align-items: center;
    gap: 10px;
    font-size: 14px;
    color: var(--ink);
  }
  .contact-line svg { width: 17px; height: 17px; fill: var(--ink); }
  .contact-line .divider {
    width: 2px;
    height: 15px;
    background: var(--ink);
    margin: 0 8px;
  }
  .address-line {
    margin-top: 10px;
    font-size: 14px;
    letter-spacing: 1.6px;
    color: var(--ink);
  }
  .web-line {
    margin-top: 8px;
    font-size: 14px;
    letter-spacing: 5px;
    color: var(--brand-teal);
  }
  .card-back {
    background: var(--brand-teal);
    display: flex;
    align-items: center;
    justify-content: center;
  }
  .brand-name {
    font-weight: 500;
    font-size: 68px;
    color: var(--card-white);
    letter-spacing: 2px;
  }
</style>
</head>
<body>
  <main class="canvas">
    <section class="card card-front">
      <div class="frame"></div>
      <h1 class="person-name">Daniel Ormsby</h1>
      <div class="name-rule"></div>
      <p class="contact-line">
        <svg viewBox="0 0 24 24" aria-hidden="true"><path d="M6.6 10.8a15.1 15.1 0 0 0 6.6 6.6l2.2-2.2a1 1 0 0 1 1-.25 11.4 11.4 0 0 0 3.6.57 1 1 0 0 1 1 1V20a1 1 0 0 1-1 1A17 17 0 0 1 3 4a1 1 0 0 1 1-1h3.5a1 1 0 0 1 1 1c0 1.25.2 2.45.57 3.57a1 1 0 0 1-.25 1z"/></svg>
        <span>+82 5550 2417 36</span>
        <span class="divider"></span>
        <svg viewBox="0 0 24 24" aria-hidden="true"><path d="M2 5h20v14H2z M3.5 6.5 12 13l8.5-6.5" fill="none" stroke="#1c1c1c" stroke-width="0"/><path d="M2 5h20v14H2zm2 1.6V17h16V6.6l-8 6.1z"/><path d="M3.2 5.5h17.6L12 12.2z"/></svg>
        <span>hello@lodgepair.com</span>
      </p>
      <p class="address-line">2870 Harbor Lane Unit 318, Zip Code 450117</p>
      <p class="web-line">lodgepair.com</p>
    </section>
    <section class="card card-back">
      <span class="brand-name">QUELZO</span>
    </section>
  </main>
</body>
</html>
```